Business Name is TL Glamworks - Make-up Artist

I'm looking for an attractive and eye catching business card for for mobile make-up artist business. On the front of the card, I just want the name TL Glamworks in feminine type cursive writing and underneath my name Tessa Lowrie and Make-Up Artist.
On the back of the card, I would like written down one side the following;
Make-Up Tutorials
Bridal
Photography
Debutante
Formals
Family Portraits
I would also like the following details as well as the Chatterbook and Snapgram Icons;
Mobile: 0462 318 725
Email: tessalowrie@mailbox-demo.com
Website: tessalowrie.velmora-demo.com
Certificate III in Make-Up
Also, I would like a section that says Your Next Appointment and a space to put that information.
I would also like the Velmora Symbol on the bottom right hand corner (I have attached)

Target Market(s)

Mostly females

Industry/Entity Type

Makeup

Contact Information for Business Card

TL Glamworks
Tessa Lowrie - Make-Up Artist

Font styles to use
Script

Colors
b768aa
886aae
e34297

Requirements
Must have
• Mobile: 0462 318 725
• Email: tessalowrie@mailbox-demo.com
• Website: tessalowrie.velmora-demo.com
• Certificate III in Make-Up
Nice to have
• Something to do with make-up like a smudged lipstick or some eye shadow
Should not have
• Don't want it too busy

```html
<!DOCTYPE html>
<html lang="en">
<head>
<meta charset="utf-8">
<title>TL Glamworks – Business Card</title>
<link rel="stylesheet" href="https://fonts.googleapis.com/css2?family=Great+Vibes&family=Lato:wght@400;700&display=swap">
<style>
  :root {
    --pink: #e2449a;
    --white: #ffffff;
    --ink: #3c3c3c;
    --grey: #4b4b4b;
    --green: #2e7d3a;
    --backdrop: #ecebe8;
    --script: "Great Vibes", cursive;
    --sans: "Lato", Arial, sans-serif;
  }
  * { box-sizing: border-box; margin: 0; padding: 0; }
  html, body { width: 1200px; height: 900px; overflow: hidden; }
  body { background: var(--backdrop); font-family: var(--sans); position: relative; }

  .card {
    position: absolute;
    left: 280px;
    width: 640px;
    height: 390px;
    overflow: hidden;
    box-shadow: 0 6px 18px rgba(0,0,0,.18);
  }
  .card--front { top: 40px; background: var(--pink); }
  .card--back  { top: 470px; background: var(--white); }

  /* Front */
  .front__brand { position: absolute; top: 50px; right: 100px; text-align: center; color: var(--white); }
  .brand-script { font-family: var(--script); font-size: 72px; line-height: 1; font-weight: 400; white-space: nowrap; }
  .brand-sub { font-size: 19px; letter-spacing: 1.2px; text-transform: uppercase; margin-top: 2px; white-space: nowrap; }

  .front__appointment {
    position: absolute; left: 0; right: 0; top: 248px; height: 86px;
    background: var(--white);
    display: flex; align-items: center; padding-left: 40px;
    font-size: 23px; color: var(--ink);
  }
  .appointment__line { display: inline-block; width: 260px; border-bottom: 1.5px solid var(--ink); margin-left: 12px; height: 22px; }

  .front__partner {
    position: absolute; right: 28px; top: 168px; width: 112px; height: 80px;
    background: var(--white);
    display: flex; align-items: center; justify-content: center; gap: 6px;
    color: var(--green); font-size: 17px; font-weight: 700;
  }
  .partner__dot { width: 14px; height: 14px; border-radius: 50%; background: var(--green); }

  /* Back */
  .back__wave { position: absolute; left: 0; top: 0; width: 640px; height: 390px; }

  .back__social { position: absolute; top: 22px; right: 24px; display: flex; gap: 14px; }
  .social { display: flex; align-items: center; gap: 5px; font-size: 13px; color: var(--pink); }
  .social__ring { width: 22px; height: 22px; border: 2px solid var(--pink); border-radius: 50%; }

  .back__services { position: absolute; top: 60px; left: 34px; font-size: 20px; line-height: 26px; color: var(--ink); }
  .sep { color: var(--pink); margin: 0 4px; }

  .back__brand { position: absolute; top: 120px; right: 28px; text-align: center; color: var(--pink); }
  .back__brand .brand-script { font-size: 60px; }
  .back__brand .brand-sub { font-size: 16px; color: var(--grey); }

  .back__contact { position: absolute; left: 30px; top: 206px; list-style: none; font-size: 18px; color: var(--ink); }
  .back__contact li { display: flex; align-items: center; gap: 8px; height: 26px; }
  .back__contact svg { width: 16px; height: 16px; flex: none; }

  .back__cert { position: absolute; right: 22px; top: 256px; color: var(--white); font-size: 16px; }
</style>
</head>
<body>

<section class="card card--front" aria-label="Card front">
  <div class="front__brand">
    <h1 class="brand-script">TL Glamworks</h1>
    <p class="brand-sub">Tessa Lowrie - Make-Up Artist</p>
  </div>
  <div class="front__partner"><span class="partner__dot"></span>Velmora</div>
  <div class="front__appointment">Your Next Appointment <span class="appointment__line"></span></div>
</section>

<section class="card card--back" aria-label="Card back">
  <svg class="back__wave" viewBox="0 0 640 390" aria-hidden="true">
    <path d="M0 336 C150 344 320 314 430 250 C330 332 160 362 0 362 Z" fill="var(--grey)"/>
    <path d="M0 368 C170 378 330 320 440 240 C520 200 590 196 640 196 L640 390 L0 390 Z" fill="var(--pink)" stroke="var(--white)" stroke-width="3"/>
  </svg>

  <div class="back__social">
    <span class="social"><span class="social__ring"></span>Chatterbook</span>
    <span class="social"><span class="social__ring"></span>Snapgram</span>
  </div>

  <p class="back__services">
    Make-Up Tutorials<span class="sep">|</span>Bridal<span class="sep">|</span>Photography<br>
    Debutante<span class="sep">|</span>Formals<span class="sep">|</span>Family Portraits
  </p>

  <div class="back__brand">
    <h2 class="brand-script">TL Glamworks</h2>
    <p class="brand-sub">Tessa Lowrie - Make-Up Artist</p>
  </div>

  <ul class="back__contact">
    <li>
      <svg viewBox="0 0 16 16"><rect x="3" y="1" width="10" height="14" rx="2" fill="none" stroke="var(--pink)" stroke-width="1.8"/><circle cx="8" cy="12" r="1" fill="var(--pink)"/></svg>
      0462 318 725
    </li>
    <li>
      <svg viewBox="0 0 16 16"><rect x="1" y="3" width="14" height="10" fill="var(--pink)"/><path d="M1 3 L8 9 L15 3" fill="none" stroke="var(--white)" stroke-width="1.4"/></svg>
      tessalowrie@mailbox-demo.com
    </li>
    <li>
      <svg viewBox="0 0 16 16"><circle cx="8" cy="8" r="7" fill="var(--pink)"/><path d="M1 8 H15 M8 1 C4 5 4 11 8 15 M8 1 C12 5 12 11 8 15" fill="none" stroke="var(--white)" stroke-width="1"/></svg>
      tessalowrie.velmora-demo.com
    </li>
  </ul>

  <p class="back__cert">Certificate III in Make-Up</p>
</section>

</body>
</html>
```